Small Web Design for Boat Industry

We are looking for a small 4 page web site. The designs will need to be clean and stylish. Please see samples of sites that we like.

http://www.veltrani.co.uk/
http://quillmarsh.com/

We need a quick turnaround.

Requirements
Must have
• Please see attached documents with all wording and images

```html
<!DOCTYPE html>
<html lang="en">
<head>
<meta charset="utf-8">
<title>Berth-Link FAQs</title>
<link href="https://fonts.googleapis.com/css2?family=Arimo:wght@400;700&display=swap" rel="stylesheet">
<style>
:root{
  --page:#ffffff;
  --text:#8b8f90;
  --heading:#858d8f;
  --accent:#6aa9aa;
  --nav:#8a8f92;
  --brand:#2f6fa6;
  --band-outer:#f3dfe0;
  --band-inner:#ebc4c5;
  --foot-outer:#444f56;
  --foot-inner:#4c4a4b;
  --foot-text:#ffffff;
  --foot-muted:#8f8f8f;
}
*{margin:0;padding:0;box-sizing:border-box}
html,body{width:900px;height:1200px;overflow:hidden;background:var(--page)}
body{font-family:"Arimo",Arial,sans-serif;position:relative}
.site-header{position:absolute;top:0;left:0;width:900px;height:108px;background:var(--page);box-shadow:0 2px 8px rgba(0,0,0,.12);z-index:2}
.brand{position:absolute;left:100px;top:30px;display:flex;align-items:center;gap:8px;font-size:25px;font-weight:700;color:var(--brand);letter-spacing:-.5px}
.brand-dot{width:12px;height:12px;border-radius:50%;background:var(--brand)}
.main-nav a{position:absolute;top:46px;font-size:11.5px;font-weight:700;letter-spacing:2.6px;color:var(--nav);text-decoration:none}
.main-nav a.is-active{color:var(--accent)}
.faq{position:absolute;top:138px;left:115px;width:670px;text-align:center}
.faq-title{font-size:13px;font-weight:700;color:var(--heading);line-height:20px}
.faq-rule{display:block;margin:12px auto 16px;width:354px;height:4px}
.faq h2{font-size:13px;font-weight:700;color:var(--heading);line-height:18px;margin-bottom:7px}
.faq p{font-size:11px;font-weight:700;color:var(--text);line-height:17.7px;margin-bottom:5px}
.faq p.closing{margin-top:30px}
.band{position:absolute;top:984px;left:0;width:900px;height:56px;background:var(--band-outer)}
.band-inner{position:absolute;left:79px;width:740px;height:56px;background:var(--band-inner)}
.site-footer{position:absolute;top:1040px;left:0;width:900px;height:160px;background:var(--foot-outer)}
.footer-inner{position:absolute;left:79px;width:740px;height:160px;background:var(--foot-inner)}
.footer-col{position:absolute;top:24px;list-style:none;font-size:9.5px;font-weight:700;letter-spacing:2px;color:var(--foot-text)}
.footer-col li{height:22px}
.footer-links{left:225px}
.footer-contact{left:348px}
.copyright{position:absolute;top:129px;width:740px;text-align:center;font-size:9.5px;font-weight:700;color:var(--foot-muted)}
</style>
</head>
<body>
<header class="site-header">
  <div class="brand"><span>Berth-Link.com</span><span class="brand-dot"></span></div>
  <nav class="main-nav">
    <a class="is-active" style="left:327px">FAQ'S</a>
    <a style="left:431px">VIDEOS</a>
    <a style="left:546px">CONTACT US</a>
    <a style="left:708px">BUY NOW</a>
  </nav>
</header>

<main class="faq">
  <h1 class="faq-title">FAQs</h1>
  <svg class="faq-rule" viewBox="0 0 354 4" aria-hidden="true">
    <defs><linearGradient id="rule" x1="0" x2="1"><stop offset="0" stop-color="#ccc" stop-opacity="0"/><stop offset=".5" stop-color="#bbb"/><stop offset="1" stop-color="#ccc" stop-opacity="0"/></linearGradient></defs>
    <rect width="354" height="2" fill="url(#rule)"/>
  </svg>

  <h2>Do you ship internationally?</h2>
  <p>We do. Of course there will be additional charges. Call or contact us for the actual cost.</p>

  <h2>Do these work on all docks?</h2>
  <p>Most but not all. Berth-Links can be adapted to work in most situations. You can use rope to extend or change the method of connection. The important factor is the angle of use. They must have the opportunity to extend and contract, so if the angle is too steep or the distance between the boat and cleat is too short they will not function properly.</p>

  <h2>How do I connect these to my boat and the dock?</h2>
  <p>Start by matching a cleat on the dock and a cleat on your boat. Make the connection with the double loop Berth-Link by stretching the cable over the cleats or through and around the cleats. Then find a point on your boat to match a second tie up. We sell a split end with clip locks to add flexibility if needed. You can use this end on any other load bearing point on your boat or dock like a rail or a tower. When possible tie the split cable in a half knot around the point of connection (this will keep most of<br>the strain on the cable rather than the clips). Then use the double-hole clip to join the cables and the single hole clip to prevent any slipping. A dock line or two can then be used if necessary to keep the boat from swinging or moving too far forward or back. In many situations this is not needed but care should be taken to ensure the boats security. Berth-Links can be used on the same side or one on each side. Use your judgement when deciding the best method placement and connection.</p>

  <h2>Can I use your product to permanently connect my boat to my dock?</h2>
  <p>Berth-Links were designed for the temporary docking of your boat. If the dock is sheltered from the elements then the long term use should not be a problem. As always use common sense when making this decision. Berth-Links can be used in conjunction with ropes and fenders. Anytime there are adverse conditions use all precautions to secure your boat and protect it from damage as Berth-Link is not responsible for any damage that may occur.</p>

  <h2>I have a 28 ft. boat. Will these work for me?</h2>
  <p>Berth-Links will work best on boats less than 25 feet, however they have been used on boats much larger. It depends on the relationship between your boat and the dock. As mentioned previously, the angle between the boat and the dock must allow the extension and contraction of the units to be fully effective.<br>Will these replace the need for fenders.<br>They can but you must use your judgement on whether or not they should.</p>

  <h2>Will Berth-Links damage or scar my boat?</h2>
  <p>If used as directed they will not. The end caps are made of composite rubber and the cable is nylon wrapped to protect your boat. They were designed not to scratch your boat.</p>

  <h2>Will they float if dropped in the water?</h2>
  <p>Yes. They have a foam cover that allows them to float. We have also added a replaceable nylon netting to protect the foam cover.</p>

  <p class="closing">We love the opportunity to answer your questions about our product. We realize that Berth-Links are new to most of you.<br>So please contact us by the phone or through our Contact Page on our site with any more questions.</p>
</main>

<div class="band"><div class="band-inner"></div></div>

<footer class="site-footer">
  <div class="footer-inner">
    <ul class="footer-col footer-links">
      <li>FAQ'S</li><li>VIDEOS</li><li>CONTACT US</li><li>BUY NOW</li>
    </ul>
    <ul class="footer-col footer-contact">
      <li>18 HARBOURLINE ROAD</li><li>WESTBAY VICTORIA, 3099</li><li>+61 3 5550 1287</li><li>HELLO@BERTH-LINK.COM</li>
    </ul>
    <p class="copyright">Copyright © 2013. All Rights Reserved</p>
  </div>
</footer>
</body>
</html>
```